Brightstep Podiatry Needs a Branded 8.5 x 11 template

We need a single template that will reflect our brand and have a really interesting and catchy feel. Be creative. It should include our logo a catch phrase like "Where Your Feet Are in Good Hands" and editable. There should be a header with this information. The central portion should be available to place text about medical conditions or other information and available to take pictures.
The footer needs to be all of the info on our location such as address, phone, drs names etc. - see must haves
We like shadows, 3D, really creative and catchy.
Below is an example that my friend uses. I like it but would like something a little more interesting. I do not want the same design as the flyer attached.
Logo is attached.
Our Colors: Want plenty of white space
#FAC000
#9F38AA

Target Market(s)

Patients and Physicians. We are podiatrists, foot and ankle specialists but I do not want any pictures of feet or medical stuff on the template.

Industry/Entity Type

Medical

Requirements
Must have
• For the Footer: Make it creative please

Physicians and Surgeons of the Foot and Ankle
Dr. Owen Pruitt
Dr. Carla Wendham
Address 4726 W. Bellrose Ave. Suite 418, Tampa, FL 33614
phone - 813-642-0917
email office@brightsteppodiatrymail.com
web http://www.theGulfcrestFootDoc.com

The Tagline section in the header needs to be editable so I can make changes. The middle section also needs to be editable.

I prefer to make edits in Photoshop or possibly Illustrator

```html
<!DOCTYPE html>
<html lang="en">
<head>
<meta charset="utf-8">
<title>Brightstep Podiatry – Letter Template</title>
<link rel="stylesheet" href="https://fonts.googleapis.com/css2?family=Cinzel:wght@500;700&display=swap">
<style>
  :root {
    --brand-yellow: #fac000;
    --header-yellow: #f8be00;
    --brand-purple: #9f38aa;
    --deep-purple: #5a1f6a;
    --panel-edge: #c97a55;
    --panel-mid: #e4a033;
    --footer-purple: #9a6aa6;
    --footer-rose: #c98a86;
    --paper: #ffffff;
  }
  * { box-sizing: border-box; margin: 0; padding: 0; }
  html, body {
    width: 1200px; height: 900px; overflow: hidden;
    background: var(--paper);
    font-family: "Cinzel", "Times New Roman", serif;
  }
  .page { position: relative; width: 1200px; height: 900px; }

  /* Header */
  .header-band {
    position: absolute; left: 94px; top: 56px; width: 1012px; height: 139px;
    background: linear-gradient(180deg, #f2b800 0%, var(--header-yellow) 50%, #f6bb00 100%);
  }
  .header-fade {
    position: absolute; left: 94px; top: 195px; width: 1012px; height: 48px;
    background: linear-gradient(180deg, #c9c9c9 0%, #efefef 45%, var(--paper) 100%);
  }
  .brand {
    position: absolute; left: 124px; top: 100px;
    display: flex; align-items: center; gap: 12px;
  }
  .brand-mark {
    flex: none; width: 30px; height: 30px; background: var(--brand-purple);
  }
  .brand-name {
    font-weight: 700; font-size: 26px; line-height: 1.1; color: var(--brand-purple);
    letter-spacing: 0.5px;
  }
  .brand-name span { display: block; }
  .tagline {
    position: absolute; left: 455px; top: 110px;
    font-weight: 700; font-size: 30px; line-height: 1; color: var(--brand-purple);
    letter-spacing: 0.3px; white-space: nowrap;
  }

  /* Content area */
  .content-panel {
    position: absolute; left: 94px; top: 255px; width: 1012px; height: 415px;
    background: radial-gradient(ellipse 60% 70% at 50% 48%, var(--brand-yellow) 0%, var(--panel-mid) 60%, var(--panel-edge) 100%);
    box-shadow: 0 14px 16px -6px rgba(0,0,0,0.35);
  }

  /* Footer */
  .footer-bar {
    position: absolute; left: 94px; top: 730px; width: 1012px; height: 108px;
    background: linear-gradient(90deg, var(--footer-purple) 0%, var(--footer-rose) 35%, #e9a545 55%, var(--brand-yellow) 75%, #f2b400 100%);
    box-shadow: 0 4px 6px rgba(0,0,0,0.35);
  }
  .footer-title, .doctor, .address {
    position: absolute; color: var(--brand-yellow); font-weight: 700;
    white-space: nowrap; line-height: 1;
    text-shadow: 0 0 1px var(--deep-purple), 0 0 1px var(--deep-purple);
  }
  .footer-title { left: 104px; top: 737px; font-size: 22px; }
  .doctor { left: 122px; font-size: 17px; }
  .doctor::before { content: "\25BA"; color: var(--brand-purple); text-shadow: none; margin-right: 4px; }
  .doctor-1 { top: 760px; }
  .doctor-2 { top: 778px; }
  .address { left: 102px; top: 804px; font-size: 19px; display: flex; align-items: center; gap: 5px; }
  .contact {
    position: absolute; left: 655px; display: flex; align-items: center; gap: 10px;
    color: var(--brand-purple); font-weight: 700; white-space: nowrap; line-height: 1;
  }
  .contact svg { flex: none; }
  .contact-phone { top: 759px; font-size: 18px; color: var(--deep-purple); }
  .contact-email { top: 787px; font-size: 16px; }
  .contact-web { top: 813px; font-size: 16px; }
</style>
</head>
<body>
<main class="page">
  <header>
    <div class="header-band" role="img" aria-label="Yellow header band with soft rounded tile pattern"></div>
    <div class="header-fade"></div>
    <div class="brand">
      <span class="brand-mark"></span>
      <p class="brand-name"><span>Brightstep</span><span>Podiatry</span></p>
    </div>
    <p class="tagline">Where Your Feet Are In Good Hands</p>
  </header>

  <section class="content-panel" aria-label="Editable content area"></section>

  <footer>
    <div class="footer-bar" role="img" aria-label="Footer band with soft purple to yellow blurred light backdrop"></div>
    <p class="footer-title">Physicians and Surgeons of the Foot and Ankle</p>
    <p class="doctor doctor-1">Dr. Owen Pruitt</p>
    <p class="doctor doctor-2">Dr. Carla Wendham</p>
    <p class="address">
      <svg width="18" height="16" viewBox="0 0 18 16" aria-hidden="true">
        <path d="M9 1a5 5 0 0 0-5 5c0 4 5 9 5 9s5-5 5-9a5 5 0 0 0-5-5z" fill="var(--brand-yellow)" stroke="var(--deep-purple)" stroke-width="1"/>
        <circle cx="9" cy="6" r="1.8" fill="var(--deep-purple)"/>
      </svg>
      4726 W. Bellrose Ave. Suite 418, Tampa, FL 33614
    </p>
    <p class="contact contact-phone">
      <svg width="34" height="24" viewBox="0 0 34 24" aria-hidden="true">
        <rect x="4" y="1" width="26" height="22" rx="4" fill="var(--brand-purple)"/>
        <path d="M14 6c-2 3-2 9 2 12l2-2-2-2c-1-1-1-3 0-4l2-2-2-2z" fill="var(--brand-yellow)"/>
      </svg>
      813-642-0917
    </p>
    <p class="contact contact-email">
      <svg width="34" height="22" viewBox="0 0 34 22" aria-hidden="true">
        <rect x="2" y="2" width="30" height="18" fill="none" stroke="var(--brand-purple)" stroke-width="2"/>
        <path d="M2 2l15 11L32 2M2 20l11-9M32 20L21 11" fill="none" stroke="var(--brand-purple)" stroke-width="2"/>
      </svg>
      office@brightsteppodiatrymail.com
    </p>
    <p class="contact contact-web">
      <svg width="34" height="26" viewBox="0 0 34 26" aria-hidden="true">
        <g fill="none" stroke="var(--brand-purple)" stroke-width="2">
          <circle cx="17" cy="13" r="11"/>
          <ellipse cx="17" cy="13" rx="5" ry="11"/>
          <path d="M6 13h22M8 7h18M8 19h18"/>
        </g>
      </svg>
      http://www.theGulfcrestFootDoc.com
    </p>
  </footer>
</main>
</body>
</html>
```